Website for an AdOps/Media Agency

We need a logo for an ad operations firm. We help websites to maximize their advertising revenues by optimizing their ad networks, configurations, technologies, etc. The name is Brovilo, or BroVilo, to communicate that we take them to the top of their revenue potential. We want to also communicate, trust us to handle your adops, we take care of the hassle (it's an industry in continual technological innovation -- hard to stay on top of, and heavily manual, reporting, etc) and make sure our clients maximize ad revenues. For more info on site ideas/desires: https://files.quenmarto.com/doc/d/7XtRbnqLwe2Mz84PdkaHsYVoJcFuT3iGeZ5_rxOqNl/view?usp=sharing

Project Deadline Extended Reason: Apologies, I got caught up in other things. This is now priority, and will be guaranteed. I will also include an extra coding fee for a WP site and increase the budget. Thanks for your understanding! Added Thursday, July 7, 2016

Target Market(s)

Ad Operations/Media Consultancy

Industry/Entity Type

Ad Agency

Number of Pages Required

1 page

Font styles to use
Sans Serif

Requirements
Must have
• I like clean and simple, nice images, scrolling down.
Nice to have
• I like clean, fresh white running through the site. Note, I listed us as an ad agency, but only because there was no adops. We work with ad agencies, but we are more agents for publishers.
Should not have
• To much clutter.

```html
<!DOCTYPE html>
<html lang="en">
<head>
<meta charset="UTF-8">
<title>BroVilo – Contact Us</title>
<link rel="stylesheet" href="https://fonts.googleapis.com/css2?family=Questrial&family=Arimo:wght@400;700&display=swap">
<style>
  :root {
    --orange: #ff8a00;
    --ink: #2e2e2e;
    --label: #8a8a8a;
    --field-border: #b9b9b9;
    --white: #ffffff;
    --footer-bg: #333333;
    --footer-text: #9a9a9a;
    --logo-box: #2f2f2f;
  }
  * { box-sizing: border-box; margin: 0; padding: 0; }
  html, body { width: 1200px; height: 926px; overflow: hidden; background: var(--white); }
  body { position: relative; font-family: "Questrial", sans-serif; }

  .site-header { position: absolute; left: 0; top: 0; width: 1200px; height: 79px; background: var(--white); }
  .brand { position: absolute; left: 91px; top: 0; height: 79px; display: flex; align-items: center; gap: 10px; }
  .brand-square { width: 84px; height: 79px; background: var(--logo-box); }
  .brand-name { font-family: "Questrial", sans-serif; font-size: 52px; color: var(--ink); letter-spacing: 4px; }

  .main-nav { position: absolute; top: 31px; left: 0; }
  .main-nav a { position: absolute; white-space: nowrap; font-size: 16px; color: var(--ink); text-decoration: none; }
  .nav-home { left: 527px; }
  .nav-about { left: 620px; }
  .nav-services { left: 716px; }
  .nav-contact { left: 830px; }
  .nav-contact::after { content: ""; position: absolute; left: 0; right: 0; top: 28px; height: 3px; background: var(--orange); }

  .btn { position: absolute; background: var(--orange); color: var(--white); font-family: "Arimo", sans-serif; border-radius: 3px; display: flex; align-items: center; justify-content: center; gap: 14px; text-decoration: none; border: none; }
  .btn-consult { left: 980px; top: 18px; width: 158px; height: 43px; font-size: 17px; }
  .btn svg { width: 8px; height: 12px; }

  .hero { position: absolute; left: 0; top: 79px; width: 1200px; height: 221px;
    background: linear-gradient(100deg, #7a5230 0%, #b8804a 30%, #d29a5e 55%, #9a6a3c 80%, #6e4a2a 100%); }
  .hero-title-box { position: absolute; left: 324px; top: 88px; width: 579px; height: 93px; background: rgba(120,110,100,0.55);
    display: flex; align-items: center; justify-content: center; }
  .hero-title { font-family: "Arimo", sans-serif; font-weight: 700; font-size: 53px; color: var(--white); letter-spacing: 1px; white-space: nowrap; }

  .contact-form .field-label { position: absolute; font-size: 16px; color: var(--label); letter-spacing: 1.2px; }
  .contact-form .field { position: absolute; width: 251px; height: 21px; border: 1px solid var(--field-border); border-radius: 3px; background: var(--white); }
  .contact-form .select { font-size: 13px; color: var(--label); letter-spacing: 0.8px; padding-left: 24px; line-height: 19px; }
  .contact-form .select svg { position: absolute; right: 9px; top: 6px; width: 9px; height: 7px; }
  .col-left { left: 293px; }
  .col-right { left: 640px; }
  .btn-submit { left: 515px; top: 781px; width: 158px; height: 44px; font-size: 18px; gap: 24px; }

  .site-footer { position: absolute; left: 0; top: 874px; width: 1200px; height: 52px; background: var(--footer-bg);
    display: flex; align-items: center; justify-content: center; font-family: "Arimo", sans-serif; font-size: 17.5px; color: var(--footer-text); }
</style>
</head>
<body>
  <header class="site-header">
    <div class="brand">
      <div class="brand-square"></div>
      <span class="brand-name">Brovilo</span>
    </div>
    <nav class="main-nav">
      <a class="nav-home" href="#">HOME</a>
      <a class="nav-about" href="#">ABOUT</a>
      <a class="nav-services" href="#">SERVICES</a>
      <a class="nav-contact" href="#">CONTACT US</a>
    </nav>
    <a class="btn btn-consult" href="#">Free Consult
      <svg viewBox="0 0 8 12"><path d="M1.5 1 L6 6 L1.5 11" fill="none" stroke="#fff" stroke-width="2"/></svg>
    </a>
  </header>

  <section class="hero" role="img" aria-label="Photo of people meeting at a wooden table with a notebook, coffee cup, glass of water, phones and a tablet">
    <div class="hero-title-box"><h1 class="hero-title">Let’s Keep in Touch</h1></div>
  </section>

  <form class="contact-form">
    <span class="field-label" style="left:276px; top:364px;">First Name:</span>
    <div class="field col-left" style="top:396px;"></div>
    <span class="field-label" style="left:624px; top:364px;">Last Name:</span>
    <div class="field col-right" style="top:396px;"></div>

    <span class="field-label" style="left:277px; top:461px;">Company Name:</span>
    <div class="field col-left" style="top:493px;"></div>
    <span class="field-label" style="left:623px; top:461px;">Position:</span>
    <div class="field select col-right" style="top:493px;">Please Select
      <svg viewBox="0 0 9 7"><path d="M0 0 H9 L4.5 7 Z" fill="#777"/></svg></div>

    <span class="field-label" style="left:276px; top:566px;">Email Address:</span>
    <div class="field col-left" style="top:597px;"></div>
    <span class="field-label" style="left:624px; top:566px;">Geography:</span>
    <div class="field select col-right" style="top:597px;">Please Select
      <svg viewBox="0 0 9 7"><path d="M0 0 H9 L4.5 7 Z" fill="#777"/></svg></div>

    <span class="field-label" style="left:386px; top:670px;">Industry:</span>
    <div class="field select" style="left:410px; top:702px; width:363px;">Please Select
      <svg viewBox="0 0 9 7"><path d="M0 0 H9 L4.5 7 Z" fill="#777"/></svg></div>

    <button class="btn btn-submit" type="submit">SUBMIT
      <svg viewBox="0 0 8 12"><path d="M1.5 1 L6 6 L1.5 11" fill="none" stroke="#fff" stroke-width="2"/></svg>
    </button>
  </form>

  <footer class="site-footer">© 2016 BroVilo. All rights reserved. Terms of Service | Privacy Policy</footer>
</body>
</html>
```